FR banner

we need a banner design (36"x120" horizontal) that will be displayed on a local high school baseball field. My company ( Crestwell Prints Co) has been producing signage for the Fernmoor Ridge community since 2009. We would like to communicate that we do more than banners. The final design should include the slogan "Signs Shirts Swag" and our Logo.

Target Market(s)

companies, teams, events, shirt and other marketing items.

Industry/Entity Type

Sign, Print,

Font styles to use
Sans Serif

Requirements
Should not have
• no baseball content.

```html
<!DOCTYPE html>
<html lang="en">
<head>
<meta charset="utf-8">
<title>Crestwell Prints Co — Field Banner</title>
<link rel="stylesheet" href="https://fonts.googleapis.com/css2?family=Bebas+Neue&family=Exo+2:wght@700;800&display=swap">
<style>
  :root {
    --page: #ffffff;
    --panel-grey: #e6e7e9;
    --navy-light: #2b3090;
    --navy-deep: #1b1d5a;
    --ink-blue: #2f3285;
    --white: #ffffff;
    --mark: #0b0b0d;
  }
  html, body {
    margin: 0;
    padding: 0;
    width: 1200px;
    height: 1178px;
    overflow: hidden;
    background: var(--page);
  }
  .canvas {
    position: relative;
    width: 1200px;
    height: 1178px;
  }
  .field-banner {
    position: absolute;
    left: 20px;
    top: 415px;
    width: 1160px;
    height: 348px;
    display: block;
  }
  .company-name {
    font-family: "Bebas Neue", Impact, sans-serif;
    fill: var(--ink-blue);
    font-size: 84px;
    letter-spacing: 1px;
  }
  .brand-name {
    font-family: "Exo 2", Arial, sans-serif;
    font-weight: 800;
    fill: var(--white);
    font-size: 30px;
    letter-spacing: 1px;
  }
  .slogan {
    font-family: "Exo 2", Arial, sans-serif;
    font-weight: 800;
    fill: var(--white);
    font-size: 92px;
    letter-spacing: 1px;
  }
</style>
</head>
<body>
<main class="canvas">
  <svg class="field-banner" viewBox="0 0 1160 348" xmlns="http://www.w3.org/2000/svg" aria-label="Crestwell Prints Co banner: Signs Shirts Swag">
    <defs>
      <linearGradient id="navy-field" x1="0" y1="0" x2="1" y2="0">
        <stop offset="0" stop-color="var(--navy-light)"/>
        <stop offset="1" stop-color="var(--navy-deep)"/>
      </linearGradient>
    </defs>

    <!-- blue field -->
    <rect class="blue-field" x="0" y="0" width="1160" height="348" fill="url(#navy-field)"/>
    <!-- grey name panel with diagonal edge -->
    <polygon class="name-panel" points="0,0 473,0 345,308 0,308" fill="var(--panel-grey)"/>

    <!-- company name -->
    <text class="company-name" x="190" y="140" text-anchor="middle">CRESTWELL</text>
    <text class="company-name" x="190" y="228" text-anchor="middle">PRINTS CO</text>

    <!-- brand mark stand-in -->
    <g class="brand-lockup">
      <circle cx="452" cy="174" r="40" fill="var(--mark)" stroke="var(--white)" stroke-width="5"/>
      <text class="brand-name" x="506" y="166">CRESTWELL</text>
      <text class="brand-name" x="506" y="200">PRINTS CO</text>
    </g>

    <!-- slogan -->
    <text class="slogan" x="1138" y="90" text-anchor="end">SIGNS</text>
    <text class="slogan" x="1138" y="178" text-anchor="end">SHIRTS</text>
    <text class="slogan" x="1138" y="266" text-anchor="end">SWAG</text>
  </svg>
</main>
</body>
</html>
```